Lumeva Botanics Natural baby skin and hair care

We need a look and feel for a line of baby care products. A lotion, Wash and baby oil. We already have an existing line of products and are now venturing into baby care. We want a natural look with "love, softness and a touch of earth and Africa'

Industry/Entity Type

Retail

Font styles to use
Script

Colors
fbed22
f78f20
9bcb3c

Requirements
Must have
• Natural elements
Should not have
• Red, Black abstract shapes

```html
<!DOCTYPE html>
<html lang="en">
<head>
<meta charset="UTF-8">
<title>Lumeva Baby Wash Label</title>
<link href="https://fonts.googleapis.com/css2?family=Cormorant+Garamond:wght@500&family=Dancing+Script:wght@600&family=Fredoka:wght@600&family=Patrick+Hand&family=Amatic+SC:wght@700&display=swap" rel="stylesheet">
<style>
  :root {
    --bg: #ecebf0;
    --label-white: #ffffff;
    --sky-blue: #4aa8dc;
    --sky-blue-soft: #8fcbee;
    --leaf-dark: #1f6b2e;
    --leaf-light: #7cc242;
    --ink: #2b2b2b;
    --rule: #3a4a48;
  }
  html, body {
    margin: 0;
    width: 1200px;
    height: 1200px;
    overflow: hidden;
    background: var(--bg);
  }
  .label {
    position: absolute;
    left: 360px;
    top: 116px;
    width: 480px;
    height: 968px;
    background: linear-gradient(to bottom, var(--sky-blue) 0px, var(--sky-blue-soft) 50px, var(--label-white) 150px);
    overflow: hidden;
  }
  .claim {
    position: absolute;
    top: 58px;
    width: 100%;
    text-align: center;
    font-family: "Patrick Hand", cursive;
    font-size: 40px;
    letter-spacing: 2px;
    color: var(--ink);
  }
  .brand-mark {
    position: absolute;
    left: 128px;
    top: 164px;
    width: 224px;
    height: 246px;
    display: flex;
    flex-direction: column;
    align-items: center;
    justify-content: center;
    gap: 18px;
  }
  .brand-mark .mark-square {
    width: 34px;
    height: 34px;
    border: 2px solid var(--ink);
  }
  .brand-mark .brand-name {
    font-family: "Cormorant Garamond", serif;
    font-weight: 500;
    font-size: 26px;
    letter-spacing: 4px;
    color: var(--ink);
    text-align: center;
    line-height: 1.25;
  }
  .floral {
    position: absolute;
    top: 125px;
    width: 70px;
    height: 377px;
    border-radius: 35px;
    background: linear-gradient(to bottom, rgba(124,194,66,0.35), rgba(74,168,220,0.3), rgba(124,194,66,0.35));
  }
  .floral.left { left: 22px; }
  .floral.right { right: 22px; }
  .product-name {
    position: absolute;
    top: 488px;
    width: 100%;
    text-align: center;
    font-family: "Dancing Script", cursive;
    font-weight: 600;
    font-size: 66px;
    color: var(--leaf-light);
  }
  .product-type {
    position: absolute;
    top: 568px;
    width: 100%;
    text-align: center;
    font-family: "Fredoka", sans-serif;
    font-weight: 600;
    font-size: 62px;
    color: var(--leaf-dark);
    letter-spacing: 1px;
  }
  .descriptor {
    position: absolute;
    top: 694px;
    width: 100%;
    text-align: center;
    font-family: "Dancing Script", cursive;
    font-weight: 600;
    font-size: 26px;
    color: var(--ink);
  }
  .ingredients {
    position: absolute;
    top: 766px;
    width: 100%;
    text-align: center;
    font-family: "Amatic SC", cursive;
    font-weight: 700;
    font-size: 40px;
    letter-spacing: 1px;
    color: var(--leaf-light);
  }
  .rule {
    position: absolute;
    top: 884px;
    left: 0;
    width: 100%;
    height: 4px;
    background: var(--rule);
  }
  .volume-band {
    position: absolute;
    top: 888px;
    left: 0;
    width: 100%;
    height: 80px;
    background: var(--sky-blue);
    display: flex;
    align-items: center;
    justify-content: center;
    font-family: "Fredoka", sans-serif;
    font-weight: 600;
    font-size: 24px;
    letter-spacing: 2px;
    color: var(--leaf-dark);
  }
</style>
</head>
<body>
  <main class="label">
    <div class="claim">100% NATURAL</div>

    <div class="floral left" role="img" aria-label="Hand-drawn green leaves and blue flowers border"></div>
    <div class="floral right" role="img" aria-label="Hand-drawn green leaves and blue flowers border"></div>

    <div class="brand-mark">
      <div class="mark-square"></div>
      <div class="brand-name">LUMEVA<br>BOTANICS</div>
    </div>

    <div class="product-name">Lumeva</div>
    <div class="product-type">BABY WASH</div>
    <div class="descriptor">Natural Bath &amp; Body Wash</div>
    <div class="ingredients">Shea Butter &amp; Chamomile</div>

    <div class="rule"></div>
    <div class="volume-band">250ML/8OZ.</div>
  </main>
</body>
</html>
```